QV - menu design

Hi,

We require elegant menu design for upscale restaurant. Please find attached the logo and the menu items for your reference.

for inspiration, this is a good website: -
http://www.platewhisper.example/bellfoldnotes/about.php

We are very much open for Menu Size suggestions.

unfortunately the place is going under renovation, we don't have updated images to it. the closest look and feel to our place is http://varnelo.example ..

we are also open for creative options on the shape, the styles, etc. as long as it represents the fine dine feel ...

Thanks ...

Dear All,

We wouldlike to extend our apology for not being able to provide feedbacks on everysingle design. We were extremely busy and we have multiple contests opensimultaneously which makes the process even harder.

However,we would like to thank you all for the efforts you have put into designingour menu. It is very much appreciated …

We wishyou all success in your design ventures and we are quite positive that we willbe working with many of you on many projects in the soon future. 

Thanks & Regards,

TLG Team...

 

 

 

Industry/Entity Type

Restaurant

Requirements
Must have
• Please ensure that there are 'some' images in the menu ... this is very important.
Should not have
• IMPORTANT: -

1. Please DO NOT insert any currency sign to the menu
2. Please keep the prices of the menu at the end of the menu items descriptions NOT beside the menu item names. The font of the price should be similar to the menu item description and please DO NOT bold the numbers. the prices should be subtle.

Thank you ...

```html
<!DOCTYPE html>
<html lang="en">
<head>
<meta charset="utf-8">
<title>QV – Menu Design</title>
<link rel="stylesheet" href="https://fonts.googleapis.com/css2?family=Open+Sans:wght@400;700&family=Ubuntu:wght@400&display=swap">
<style>
  :root {
    --backdrop: #6e6e6e;
    --page: #f1dccc;
    --page-deep: #e8c9b2;
    --panel: #f6e6da;
    --band: #d6a480;
    --band-dark: #c18660;
    --rule: #f9ede3;
    --ink: #5a4a42;
    --ink-soft: #6d5b52;
    --badge: #f2f2f2;
    --brand-ink: #3a3a3a;
  }
  * { margin: 0; padding: 0; box-sizing: border-box; }
  html, body { width: 1200px; height: 900px; overflow: hidden; }
  body { background: var(--backdrop); font-family: "Open Sans", sans-serif; color: var(--ink); position: relative; }

  .page { position: absolute; top: 140px; height: 605px; }
  .page--left { left: 175px; width: 415px; background: linear-gradient(90deg, var(--page) 0%, var(--page-deep) 100%); }
  .page--right { left: 590px; width: 395px; background: linear-gradient(90deg, var(--page-deep) 0%, var(--page) 100%); }

  .frame-rule { position: absolute; height: 2px; background: var(--rule); }
  .base-band { position: absolute; height: 9px; background: var(--band); }

  .content-panel { position: absolute; background: var(--panel); opacity: .55; }

  .brand-badge { position: absolute; background: var(--badge); border-radius: 50%; display: flex; align-items: center; justify-content: center; }
  .brand-name { font-family: "Ubuntu", sans-serif; font-size: 13px; color: var(--brand-ink); letter-spacing: 1px; text-transform: uppercase; white-space: nowrap; text-align: center; }

  .section-tab { position: absolute; background: var(--band); font-family: "Ubuntu", sans-serif; font-size: 16px; color: var(--ink); display: flex; align-items: center; justify-content: center; }

  .item { position: absolute; width: 290px; }
  .item--soup { width: 220px; white-space: nowrap; }
  .item-name { font-size: 7.5px; font-weight: 700; line-height: 11px; }
  .item-desc { font-size: 7px; line-height: 8.5px; color: var(--ink-soft); margin-top: 5px; }
  .price { position: absolute; font-size: 7.5px; color: var(--ink-soft); white-space: nowrap; }

  .side-bar { position: absolute; background: var(--band-dark); }
</style>
</head>
<body>

<!-- Left page: breakfast -->
<section class="page page--left">
  <div class="frame-rule" style="left:0;top:10px;width:415px"></div>
  <div class="frame-rule" style="left:0;top:575px;width:415px"></div>
  <div class="base-band" style="left:45px;top:557px;width:320px"></div>
  <div class="content-panel" style="left:57px;top:130px;width:308px;height:398px"></div>

  <div class="brand-badge" style="left:25px;top:25px;width:175px;height:92px">
    <span class="brand-name">Quayside Vine Café</span>
  </div>
  <div class="section-tab" style="left:245px;top:20px;width:120px;height:30px">The Breakfast</div>

  <div class="item" style="left:67px;top:142px">
    <div class="item-name">Butter Croissant</div>
    <div class="item-desc">Served plain with a selection of two jams, a vanilla custard cream,<br>a chocolate Cream and butter curls.</div>
  </div>
  <span class="price" style="left:345px;top:170px">36</span>

  <div class="item" style="left:67px;top:193px">
    <div class="item-name">Cheese Croissant</div>
    <div class="item-desc">Crumbly freshly baked with cheese filling.</div>
  </div>
  <span class="price" style="left:345px;top:213px">29</span>

  <div class="item" style="left:67px;top:236px">
    <div class="item-name">Daily Fresh Eggs</div>
    <div class="item-desc">A choice of poached, scrambled, pan fried, omelet) all served with<br>toasted Bread, mushrooms, roasted tomatoes and chicken sausages.</div>
  </div>
  <span class="price" style="left:345px;top:265px">59</span>

  <div class="item" style="left:62px;top:288px">
    <div class="item-name">Healthy Time</div>
    <div class="item-desc">One choice of hot beverage from our cafe served with fruit salad,<br>natural Yoghurt, whole wheat bread vegetable sandwiches and<br>sugar free biscuits selection.</div>
  </div>
  <span class="price" style="left:345px;top:324px">49</span>

  <div class="item" style="left:62px;top:347px">
    <div class="item-name">Energy Time</div>
    <div class="item-desc">One choice of hot beverage from our cafe served with finger<br>chocolate muffins, Poached egg with toasted bread and crispy<br>beef bacon, crepe roll with goat Cheese and honey and finger<br>chocolate cream with salted cookies.</div>
  </div>
  <span class="price" style="left:345px;top:392px">59</span>

  <div class="item" style="left:59px;top:414px">
    <div class="item-name">Quayside Vine Time</div>
    <div class="item-desc">One choice of hot beverage from our cafe served with our<br>selection of scones, Smoked salmon and avocado sandwich,<br>roasted sausages sandwich, grilled vegetables sandwich,<br>selection of our best biscuits.</div>
  </div>
  <span class="price" style="left:345px;top:459px">59</span>

  <div class="item" style="left:57px;top:481px">
    <div class="item-name">The Arabic Breakfast</div>
    <div class="item-desc">Choice of Zattar Manakish and Cheese Manakish, served with one<br>choice of hot beverage from our cafe and fresh orange juice.</div>
  </div>
  <span class="price" style="left:345px;top:513px">59</span>
</section>

<!-- Right page: sandwiches and soup -->
<section class="page page--right">
  <div class="frame-rule" style="left:0;top:10px;width:395px"></div>
  <div class="frame-rule" style="left:0;top:575px;width:395px"></div>
  <div class="side-bar" style="left:372px;top:70px;width:6px;height:410px"></div>
  <div class="base-band" style="left:145px;top:492px;width:225px;height:5px"></div>

  <div class="section-tab" style="left:15px;top:25px;width:150px;height:30px">The Sandwiches</div>
  <div class="section-tab" style="left:36px;top:350px;width:94px;height:30px">Soup</div>

  <div class="item" style="left:58px;top:74px">
    <div class="item-name">Grilled Vegetables Sandwich</div>
    <div class="item-desc">with fresh Goat cheese and chives served with our<br>Homemade spicy garlic mayo.</div>
  </div>
  <span class="price" style="left:311px;top:97px">59</span>

  <div class="item" style="left:58px;top:126px">
    <div class="item-name">Butterfish burger</div>
    <div class="item-desc">with fresh tomato, beef bacon, grilled vegetables and bearnaise sauce.</div>
  </div>
  <span class="price" style="left:313px;top:140px">69</span>

  <div class="item" style="left:58px;top:171px">
    <div class="item-name">Tataki Tuna sandwich</div>
    <div class="item-desc">with red onion slices, stewed endives and black olives and sultanas pate.</div>
  </div>
  <span class="price" style="left:314px;top:185px">79</span>

  <div class="item" style="left:58px;top:212px">
    <div class="item-name">Beef sirloin steak sandwich</div>
    <div class="item-desc">with grain mustard, Parmesan cheese and fresh<br>Nashi pears.</div>
  </div>
  <span class="price" style="left:315px;top:236px">79</span>

  <div class="item" style="left:58px;top:260px">
    <div class="item-name">The Traditional Club sandwich</div>
    <div class="item-desc">served with French fries and vegetable chips.</div>
  </div>
  <span class="price" style="left:316px;top:274px">69</span>

  <div class="item" style="left:58px;top:296px">
    <div class="item-name">Chicken sandwich</div>
    <div class="item-desc">with Parmesan cheese slices, sundried tomatoes and mint<br>Flavored mayo.</div>
  </div>
  <span class="price" style="left:319px;top:318px">69</span>

  <div class="item item--soup" style="left:140px;top:347px">
    <div class="item-name">Bouillabaisse</div>
    <div class="item-desc">Traditional French Seafood soup, with Saffron and Estragon.</div>
  </div>
  <span class="price" style="left:350px;top:361px">119</span>

  <div class="item item--soup" style="left:140px;top:392px">
    <div class="item-name">Barley soup</div>
    <div class="item-desc">With fresh vegetables, tomato smoothie and a hint of garlic oil.</div>
  </div>
  <span class="price" style="left:358px;top:406px">49</span>

  <div class="item item--soup" style="left:140px;top:433px">
    <div class="item-name">Beef chili</div>
    <div class="item-desc">Served with Arabic bread, fresh guacamole and spicy black beans.</div>
  </div>
  <span class="price" style="left:360px;top:451px">49</span>

  <div class="brand-badge" style="left:203px;top:490px;width:190px;height:90px">
    <span class="brand-name">Quayside Vine Café</span>
  </div>
</section>

</body>
</html>
```